Gestaltung von Bilder/Icons mit den wichtigsten Fakten des Unternehmens aus 15 Jahren
Zielgruppe
Vireto Verkauft online und in Galerien Fotokunst auf höchstem Niveau. Alle Infos findet man auch online unter: https://www.vireto.de/unsere-editionen/#prinzip
Zu unserem 15-Jährigen Firmenjubiläum möchten wir eine ansprechende Infografik auf unserer Website und in den Galerien zeigen. Hier: https://www.vireto.de/15-jahre-vireto/
Beispiele sind diesem Briefing beigefügt.
Aufgabenstellung
Die Infografik soll bitte folgende Informationen verarbeiten:
536 Editionen von Künstlern verlegt
Künstlerische Freiheit mit 21.650.350 € an Honoraren gefördert
Ermöglicht durch 134 VIRETO-Mitarbeiter
28 Galerien weltweit
246.912 zufriedene Kunden
687.601 signierte, limitierte Editionen ausgeliefert
Kunstsammler in 129 Ländern beliefert
1.612 Vernissagen, Events und Lesungen
532.567 Besucher pro Jahr

```html
<!DOCTYPE html>
<html lang="de">
<head>
<meta charset="utf-8">
<title>15 Jahre Vireto – Fakten</title>
<link href="https://fonts.googleapis.com/css2?family=Roboto+Condensed:wght@300;700&display=swap" rel="stylesheet">
<style>
  :root {
    --bg: #2d2d2d;
    --ink: #ffffff;
    --placeholder: #e6e6e6;
  }
  * { margin: 0; padding: 0; box-sizing: border-box; }
  html, body { width: 1200px; height: 848px; overflow: hidden; background: var(--bg); }
  .infographic {
    position: relative;
    width: 1200px;
    height: 848px;
    background: var(--bg);
    color: var(--ink);
    font-family: "Roboto Condensed", sans-serif;
  }
  .icon { position: absolute; display: block; }
  .line {
    position: absolute;
    width: 420px;
    text-align: center;
    line-height: 1;
    white-space: nowrap;
  }
  .line--figure { font-weight: 700; font-size: 40px; letter-spacing: -0.02em; }
  .line--label { font-weight: 300; font-size: 26px; letter-spacing: -0.01em; }
  .placeholder { position: absolute; background: var(--placeholder); }
</style>
</head>
<body>
<main class="infographic">

  <!-- Editionen -->
  <svg class="icon icon-easel" style="left:201px;top:55px" width="64" height="100" viewBox="0 0 64 100" aria-hidden="true">
    <rect x="4" y="3" width="56" height="57" fill="none" stroke="var(--ink)" stroke-width="5"/>
    <circle cx="18" cy="17" r="6" fill="var(--ink)"/>
    <path d="M6 40 L20 28 L30 38 L42 22 L58 40 L58 58 L6 58 Z" fill="var(--ink)"/>
    <line x1="32" y1="60" x2="32" y2="80" stroke="var(--ink)" stroke-width="5" stroke-linecap="round"/>
    <line x1="16" y1="72" x2="48" y2="72" stroke="var(--ink)" stroke-width="5" stroke-linecap="round"/>
    <line x1="20" y1="62" x2="8" y2="96" stroke="var(--ink)" stroke-width="5" stroke-linecap="round"/>
    <line x1="44" y1="62" x2="56" y2="96" stroke="var(--ink)" stroke-width="5" stroke-linecap="round"/>
  </svg>
  <div class="line line--figure" style="left:19px;top:170px">536 EDITIONEN</div>
  <div class="line line--label" style="left:19px;top:216px">von Künstlern verlegt</div>

  <!-- Honorare -->
  <svg class="icon icon-coins" style="left:572px;top:52px" width="74" height="68" viewBox="0 0 74 68" aria-hidden="true">
    <g fill="var(--ink)" stroke="var(--bg)" stroke-width="2">
      <ellipse cx="17" cy="34" rx="16" ry="5"/><ellipse cx="17" cy="28" rx="16" ry="5"/><ellipse cx="17" cy="22" rx="16" ry="5"/>
      <ellipse cx="17" cy="16" rx="16" ry="5"/><ellipse cx="17" cy="10" rx="16" ry="5"/><ellipse cx="17" cy="5" rx="16" ry="5"/>
      <ellipse cx="37" cy="52" rx="16" ry="5"/><ellipse cx="37" cy="46" rx="16" ry="5"/><ellipse cx="37" cy="40" rx="16" ry="5"/>
      <ellipse cx="37" cy="34" rx="16" ry="5"/><ellipse cx="37" cy="28" rx="16" ry="5"/><ellipse cx="37" cy="23" rx="16" ry="5"/>
      <ellipse cx="57" cy="62" rx="16" ry="5"/><ellipse cx="57" cy="56" rx="16" ry="5"/><ellipse cx="57" cy="50" rx="16" ry="5"/>
      <ellipse cx="57" cy="44" rx="16" ry="5"/>
    </g>
  </svg>
  <div class="line line--label" style="left:401px;top:137px">Künstlerische Freiheit mit</div>
  <div class="line line--figure" style="left:401px;top:171px">21.650.350 €</div>
  <div class="line line--label" style="left:401px;top:218px">an Honoraren gefördert</div>

  <!-- Mitarbeiter -->
  <div class="line line--label" style="left:744px;top:137px">Ermöglicht durch</div>
  <div class="line line--figure" style="left:744px;top:169px">134 VIRETO-</div>
  <div class="line line--label" style="left:744px;top:216px">Mitarbeiter</div>
  <div class="placeholder" role="img" aria-label="Piktogramm: Mitarbeiter hält ein gerahmtes Bild" style="left:1078px;top:122px;width:64px;height:118px;border-radius:8px"></div>

  <!-- Kunden -->
  <div class="placeholder" role="img" aria-label="Piktogramm: zufriedener Kunde" style="left:195px;top:311px;width:58px;height:58px;border-radius:50%"></div>
  <svg class="icon icon-stars" style="left:184px;top:374px" width="80" height="24" viewBox="0 0 80 24" aria-hidden="true">
    <g fill="var(--ink)">
      <path id="star" d="M12 1 L15 9 L23 9 L17 14 L19 23 L12 18 L5 23 L7 14 L1 9 L9 9 Z"/>
      <use href="#star" x="28"/>
      <use href="#star" x="56"/>
    </g>
  </svg>
  <div class="line line--figure" style="left:10px;top:416px">246.912</div>
  <div class="line line--label" style="left:10px;top:463px">zufriedene Kunden</div>

  <!-- Galerien -->
  <svg class="icon icon-pin" style="left:585px;top:316px" width="60" height="82" viewBox="0 0 60 82" aria-hidden="true">
    <path d="M30 2 C14 2 2 14 2 30 C2 46 18 60 30 80 C42 60 58 46 58 30 C58 14 46 2 30 2 Z" fill="var(--ink)"/>
    <circle cx="30" cy="30" r="20" fill="var(--bg)"/>
    <path d="M30 14 C20 14 14 22 14 30 C14 40 22 46 30 46 C34 46 34 42 32 40 C30 37 32 34 36 34 C42 34 46 32 46 27 C46 19 39 14 30 14 Z" fill="var(--ink)"/>
    <g fill="var(--bg)">
      <circle cx="23" cy="23" r="2.6"/><circle cx="31" cy="20" r="2.6"/><circle cx="39" cy="24" r="2.6"/><circle cx="22" cy="32" r="2.6"/><circle cx="25" cy="40" r="2.6"/>
    </g>
  </svg>
  <div class="line line--figure" style="left:395px;top:416px">28 GALERIEN</div>
  <div class="line line--label" style="left:395px;top:464px">weltweit</div>

  <!-- Editionen ausgeliefert -->
  <svg class="icon icon-diamond" style="left:959px;top:310px" width="64" height="62" viewBox="0 0 64 62" aria-hidden="true">
    <g stroke="var(--ink)" stroke-width="3" stroke-linecap="butt">
      <line x1="32" y1="1" x2="32" y2="9"/>
      <line x1="15" y1="6" x2="19" y2="12"/><line x1="49" y1="6" x2="45" y2="12"/>
      <line x1="5" y1="15" x2="12" y2="19"/><line x1="59" y1="15" x2="52" y2="19"/>
      <line x1="1" y1="32" x2="10" y2="32"/><line x1="54" y1="32" x2="63" y2="32"/>
    </g>
    <path d="M22 20 L42 20 L52 32 L32 60 L12 32 Z" fill="var(--ink)"/>
    <path d="M23 24 L41 24 L47 31 L17 31 Z M18 34 L28 34 L32 50 Z M36 34 L46 34 L32 50 Z" fill="var(--bg)"/>
  </svg>
  <div class="line line--figure" style="left:779px;top:384px">687.601</div>
  <div class="line line--label" style="left:779px;top:431px">signierte, limitierte</div>
  <div class="line line--label" style="left:779px;top:464px">Editionen ausgeliefert</div>

  <!-- Länder -->
  <svg class="icon icon-globe" style="left:190px;top:569px" width="70" height="70" viewBox="0 0 70 70" aria-hidden="true">
    <g fill="none" stroke="var(--ink)" stroke-width="3">
      <circle cx="33" cy="36" r="31"/>
      <ellipse cx="33" cy="36" rx="14" ry="31"/>
      <line x1="33" y1="5" x2="33" y2="67"/>
      <line x1="2" y1="36" x2="64" y2="36"/>
      <path d="M7 20 H59 M7 52 H59"/>
    </g>
    <path d="M54 2 C47 2 43 7 43 13 C43 20 50 25 54 34 C58 25 65 20 65 13 C65 7 61 2 54 2 Z" fill="var(--ink)" stroke="var(--bg)" stroke-width="2"/>
    <circle cx="54" cy="13" r="4" fill="var(--bg)"/>
  </svg>
  <div class="line line--label" style="left:12px;top:647px">Kunstsammler in</div>
  <div class="line line--figure" style="left:12px;top:679px">129 LÄNDERN</div>
  <div class="line line--label" style="left:12px;top:725px">beliefert</div>

  <!-- Events -->
  <svg class="icon icon-cocktail" style="left:504px;top:604px" width="84" height="78" viewBox="0 0 84 78" aria-hidden="true">
    <path d="M1 15 L62 15 L34 46 Z" fill="none" stroke="var(--ink)" stroke-width="3.5" stroke-linejoin="round"/>
    <path d="M8 19 L55 19 L34 43 Z" fill="var(--ink)"/>
    <line x1="34" y1="45" x2="34" y2="73" stroke="var(--ink)" stroke-width="4"/>
    <line x1="18" y1="75" x2="50" y2="75" stroke="var(--ink)" stroke-width="5" stroke-linecap="round"/>
    <circle cx="68" cy="16" r="14" fill="var(--ink)"/>
    <circle cx="68" cy="16" r="10" fill="none" stroke="var(--bg)" stroke-width="2"/>
    <g stroke="var(--bg)" stroke-width="1.6">
      <line x1="58" y1="16" x2="78" y2="16"/><line x1="68" y1="6" x2="68" y2="26"/>
      <line x1="61" y1="9" x2="75" y2="23"/><line x1="75" y1="9" x2="61" y2="23"/>
    </g>
  </svg>
  <div class="line line--figure" style="left:581px;top:645px;width:auto;text-align:left">1.612</div>
  <div class="line line--label" style="left:413px;top:691px">Vernissagen, Events</div>
  <div class="line line--label" style="left:413px;top:725px">und Lesungen</div>

  <!-- Besucher -->
  <div class="placeholder" role="img" aria-label="Piktogramm: Gruppe von Besuchern" style="left:941px;top:590px;width:82px;height:76px;border-radius:8px"></div>
  <div class="line line--figure" style="left:771px;top:679px">532.567</div>
  <div class="line line--label" style="left:771px;top:725px">Besucher pro Jahr</div>

</main>
</body>
</html>
```